Veltrano - Mechanic/Collision Center Business Card

We're looking for a business card design for our mechanic/ collision repair shop.

Can be with colours or monochromatic.

See the attached files.

Many thanks

```html
<!DOCTYPE html>
<html lang="pt">
<head>
<meta charset="utf-8">
<title>Veltrano – Business Card</title>
<link rel="stylesheet" href="https://fonts.googleapis.com/css2?family=Roboto:wght@400;500;900&display=swap">
<style>
  :root {
    --backdrop: #3a332e;
    --card: #111112;
    --card-edge: #1c1c1e;
    --brand-blue: #2a9ad8;
    --text-light: #c9c9c9;
    --text-white: #ffffff;
    --divider: #2e2e30;
  }
  * { box-sizing: border-box; margin: 0; padding: 0; }
  html, body {
    width: 1200px; height: 844px; overflow: hidden;
    background: var(--backdrop);
    font-family: "Roboto", Arial, sans-serif;
  }
  .canvas {
    position: relative; width: 1200px; height: 844px;
    display: flex; align-items: center; justify-content: center; gap: 40px;
  }
  .card {
    width: 540px; height: 309px;
    background: var(--card);
    border: 1px solid var(--card-edge);
    box-shadow: 0 14px 30px rgba(0,0,0,.45);
    position: relative;
    display: flex;
  }
  .brand {
    display: flex; align-items: center; gap: 10px;
  }
  .brand-dot {
    width: 22px; height: 22px; border-radius: 50%;
    background: var(--brand-blue);
  }
  .brand-name {
    font-weight: 900; color: var(--text-white);
    letter-spacing: 1px;
  }

  /* Contact side */
  .card--contact .brand-zone {
    width: 50%; display: flex; align-items: center; justify-content: center;
    padding-top: 60px;
  }
  .card--contact .brand-name { font-size: 34px; }
  .card--contact .divider {
    width: 1px; background: var(--divider); margin: 24px 0;
  }
  .contact {
    flex: 1; padding: 72px 0 0 24px;
    color: var(--text-light); font-size: 15px; line-height: 19px;
  }
  .contact-name {
    color: var(--brand-blue); font-size: 17px; font-weight: 500;
    letter-spacing: .5px;
  }
  .contact-line { display: flex; align-items: center; gap: 6px; }
  .contact-line svg { width: 12px; height: 12px; fill: var(--brand-blue); flex: none; }
  .contact-company {
    color: var(--brand-blue); font-weight: 500; margin-top: 6px;
  }

  /* Brand side */
  .card--brand {
    flex-direction: column; align-items: center; justify-content: center; gap: 34px;
  }
  .card--brand .brand-name { font-size: 44px; }
  .card--brand .brand-dot { width: 28px; height: 28px; }
  .web {
    display: flex; align-items: center; gap: 8px;
    color: var(--text-light); font-size: 14px;
  }
  .web-dot {
    width: 16px; height: 16px; border-radius: 50%;
    border: 1px solid var(--text-light);
  }
</style>
</head>
<body>
<main class="canvas">
  <section class="card card--contact">
    <div class="brand-zone">
      <div class="brand">
        <span class="brand-dot"></span>
        <span class="brand-name">VELTRANO</span>
      </div>
    </div>
    <div class="divider"></div>
    <div class="contact">
      <p class="contact-name">RUI MATOS</p>
      <p>+351 910000482</p>
      <p class="contact-line">
        <svg viewBox="0 0 24 24" aria-hidden="true"><path d="M6.6 10.8a15.1 15.1 0 0 0 6.6 6.6l2.2-2.2c.3-.3.7-.4 1-.2 1.1.4 2.3.6 3.6.6.6 0 1 .4 1 1V20c0 .6-.4 1-1 1A17 17 0 0 1 3 4c0-.6.4-1 1-1h3.5c.6 0 1 .4 1 1 0 1.2.2 2.4.6 3.6.1.3 0 .7-.2 1z"/></svg>
        +351 210004715
      </p>
      <p class="contact-line">
        <svg viewBox="0 0 24 24" aria-hidden="true"><path d="M2 5h20v14H2z M2 5l10 8 10-8" stroke="#111112" stroke-width="1.5"/></svg>
        veltrano.mail@example.com
      </p>
      <p class="contact-company">Veltrano, LDA</p>
      <p>Rua das Oficinas, 14</p>
      <p>1900-000 Lisboa</p>
    </div>
  </section>

  <section class="card card--brand">
    <div class="brand">
      <span class="brand-dot"></span>
      <span class="brand-name">VELTRANO</span>
    </div>
    <p class="web"><span class="web-dot"></span>www.veltrano-oficina.pt</p>
  </section>
</main>
</body>
</html>
```